Tor Ridge Wine Club-The Onyx Roll

We are a new aspirational brand of fine Tasmania Wine. We need a commitment club poster which appeals to the ego.We have one opportunity to get customers to sign up and that is when they visit at the cellar door. This club is the core of our business.

The brand is a clean, pure , simple brand, black and white very sophiscated.
This is a top end product.

Our Commitment Club is named The Onyx Roll which is a play on words. Tradionally The Onyx Roll is a list of people that you dont want to do business with. So we are turning this on its had.

You need to make this poster sharp, desirable, possibly sexy but masculine. Im thinking Felix Crane . It doesnt matter the client will be 40 up fashion consious looking for something new , exclusive , something there peers don't have.

I dont like busy! make it clean clear and basically undeniable. The client must not be able to resist the offer.

www.torridgevines.com.au

Reason: Internet problems so cant get to respond and offer comment in a timely manner

Appreciator 40-60 male wants to be recognised fashion consious sophiscated has money and wants to part of something exclusive.

A feeling that you are part of something that only a few are. Exclusive

Maybe an imagine of beautiful people 30/40ish I want to be drinking Tor Wine / in The Onyx Roll

Fashion

Must have
• Tor Ridge Logo
TOR Bottles images

We produce only 1600 cases of wine each vintage. Therefore we have limited membership 001-999 for our club.
Award Winning Wines available exclusively from us.

Gold Member
We will reserve 2 cases of our limited vintage, to be delivered to you in May and Oct.
Single varietal or mixed cases. You receive a 15% discount.

Silver Member
We will reserve 1 case of our limited vintage to be delivered to you 6 bottles in May and 6 in Oct.
Single varietal or mixed cases. You receive a 10% discount.

To you exclusively from us not, available from any other retailers.

You will be invited to Onyx Roll Only Events and Tastings.
You will get preferential access to new and limited releases.
Members will be entered in a bi annual draw to win a 2 night stay here at the Tor Weavers Cottage on the Freycinet Coast Tasmania.

• VIP stamps,gimacs, anything that cheapens our brand.

We do not like busy posters please have white space

```html
<!DOCTYPE html>
<html lang="en">
<head>
<meta charset="utf-8">
<title>Tor Ridge Wine Club – Join The Onyx Roll</title>
<link rel="stylesheet" href="https://fonts.googleapis.com/css2?family=Cinzel:wght@400;500&family=Arimo&family=Great+Vibes&display=swap">
<style>
  :root {
    --ink: #000000;
    --paper: #ffffff;
    --gold-light: #ffd27a;
    --gold-mid: #f0a43a;
    --gold-deep: #b8650f;
    --silver-light: #d8d8d8;
    --silver-deep: #8a8a8a;
    --shadow-tone: #3a3a3a;
  }
  * { margin: 0; padding: 0; box-sizing: border-box; }
  html, body {
    width: 1200px;
    height: 900px;
    overflow: hidden;
    background: var(--ink);
  }
  .poster {
    position: relative;
    width: 1200px;
    height: 900px;
    background: var(--ink);
    color: var(--paper);
    font-family: "Arimo", Arial, sans-serif;
    overflow: hidden;
  }
  .couple-photo {
    position: absolute;
    left: 640px;
    top: 230px;
    width: 560px;
    height: 670px;
    background: radial-gradient(ellipse at 55% 35%, #4a4a4a 0%, #2a2a2a 40%, #101010 75%, var(--ink) 100%);
  }
  .brand-name {
    position: absolute;
    top: 40px;
    left: 0;
    width: 1200px;
    text-align: center;
    font-family: "Great Vibes", cursive;
    font-size: 110px;
    line-height: 130px;
    color: var(--paper);
  }
  .gold-text {
    background: linear-gradient(to bottom, var(--gold-light) 0%, var(--gold-mid) 50%, var(--gold-deep) 100%);
    -webkit-background-clip: text;
    background-clip: text;
    color: transparent;
  }
  .silver-text {
    background: linear-gradient(to bottom, var(--silver-light) 0%, var(--silver-deep) 100%);
    -webkit-background-clip: text;
    background-clip: text;
    color: transparent;
  }
  .headline {
    position: absolute;
    left: 84px;
    top: 196px;
    font-family: "Cinzel", serif;
    font-size: 54px;
    line-height: 60px;
    letter-spacing: 6.5px;
    white-space: nowrap;
  }
  .tier-title {
    position: absolute;
    left: 95px;
    font-family: "Cinzel", serif;
    font-size: 32px;
    line-height: 36px;
    letter-spacing: 4px;
    white-space: nowrap;
  }
  .tier-title--gold { top: 276px; }
  .tier-title--silver { top: 518px; left: 93px; }
  .tier-perks {
    position: absolute;
    list-style: none;
    font-size: 28px;
    line-height: 37.7px;
    letter-spacing: 0.6px;
    color: var(--paper);
  }
  .tier-perks--gold { left: 145px; top: 338px; }
  .tier-perks--silver { left: 135px; top: 573px; }
  .retail-note {
    position: absolute;
    left: 87px;
    top: 756px;
    font-size: 18px;
    letter-spacing: 0.3px;
  }
  .exclusive-line {
    position: absolute;
    left: 84px;
    top: 780px;
    font-family: "Cinzel", serif;
    font-size: 39px;
    line-height: 44px;
    letter-spacing: 5.4px;
    white-space: nowrap;
  }
  .member-benefits {
    position: absolute;
    left: 84px;
    top: 831px;
    list-style: none;
    font-size: 20px;
    line-height: 25px;
    letter-spacing: 1px;
    text-transform: uppercase;
  }
</style>
</head>
<body>
  <main class="poster">
    <div class="couple-photo" role="img" aria-label="Black and white photograph of an elegant couple in evening wear, the man in a tuxedo and bow tie"></div>

    <div class="brand-name">Tor Ridge</div>

    <h1 class="headline gold-text">JOIN THE ONYX ROLL</h1>

    <h2 class="tier-title tier-title--gold gold-text">GOLD MEMBERSHIP</h2>
    <ul class="tier-perks tier-perks--gold">
      <li>Reserve 2 cases of wine</li>
      <li>Delivered to you May 1 Oct 1</li>
      <li>You choose the variety</li>
      <li>15% discount</li>
    </ul>

    <h2 class="tier-title tier-title--silver silver-text">SILVER MEMBERSHIP</h2>
    <ul class="tier-perks tier-perks--silver">
      <li>Reserve 1/2 case of your choice wine</li>
      <li>Delivered to you May 1 Oct 1</li>
      <li>You choose you variety</li>
      <li>15% discount</li>
    </ul>

    <p class="retail-note">Not available with other retailers</p>
    <p class="exclusive-line gold-text">EXCLUSIVELY TO YOU FROM US</p>

    <ul class="member-benefits">
      <li>Preferential access to first releases and limited releases</li>
      <li>VIP access to Onyx Roll only tastings and events</li>
    </ul>
  </main>
</body>
</html>
```